Delmer's Pressure Washing Services

Starting a pressure washing business on my own in Central Valley California, not too much experience so affordable, I do houses, fences, driveways, cars, trailers, RVs. Planning to make this full-time hoping clientele picks up after having a nice business card. Design doesn't have to be flashy, more to the point, I like simplistic/personable. I do not want something exhausting to look at or with too much going on.

Target Market(s)

Residential, Commercial

Industry/Entity Type

Pressure Washing

Contact Information for Business Card

avalible Services

Font styles to use
Sans Serif

Colors
0054AA
0677BA
7BADD7
CADEEF
E8F1F8
0094D4
00A9DD
6FCCEA
C7EBF8
E9F6FB
00AB8E
00BBA5
67D7C9
C6EFE9
E9F9F6

```html
<!DOCTYPE html>
<html lang="en">
<head>
<meta charset="utf-8">
<title>Delmer's Pressure Washing Services – Business Card</title>
<link rel="stylesheet" href="https://fonts.googleapis.com/css2?family=Quicksand:wght@700&family=Source+Sans+3:wght@400&family=Montserrat:wght@400&display=swap">
<style>
  :root {
    --stage: #000000;
    --card: #38383a;
    --card-pattern: #464648;
    --teal: #00bba5;
    --blue: #0677ba;
    --text: #ffffff;
    --divider: #4a4a4c;
  }
  * { box-sizing: border-box; margin: 0; padding: 0; }
  html, body { width: 1200px; height: 900px; overflow: hidden; background: var(--stage); }
  .stage { position: relative; width: 1200px; height: 900px; }

  .card {
    position: absolute;
    width: 458px;
    height: 283px;
    background: var(--card);
    border-radius: 14px;
    overflow: hidden;
  }
  .card--front { left: 138px; top: 265px; }
  .card--back { left: 625px; top: 268px; height: 279px; }

  /* front */
  .brand {
    position: absolute;
    left: 16px; top: 100px;
    width: 200px;
    text-align: center;
  }
  .brand__dot {
    display: block;
    width: 40px; height: 40px;
    margin: 0 auto 16px;
    border-radius: 50%;
    background: var(--teal);
  }
  .brand__name {
    font-family: 'Quicksand', sans-serif;
    font-weight: 700;
    font-size: 15px;
    line-height: 1.3;
    color: var(--teal);
    white-space: nowrap;
  }
  .divider {
    position: absolute;
    left: 222px; top: 80px;
    width: 1px; height: 132px;
    background: var(--divider);
  }
  .person { position: absolute; left: 241px; top: 66px; }
  .person__name {
    font-family: 'Quicksand', sans-serif;
    font-weight: 700;
    font-size: 17px;
    color: var(--teal);
    line-height: 1.1;
  }
  .person__name .surname { color: var(--blue); }
  .person__role {
    font-family: 'Source Sans 3', sans-serif;
    font-size: 13px;
    color: var(--text);
    margin-top: 1px;
  }
  .contacts {
    position: absolute; left: 240px; top: 120px;
    list-style: none;
    font-family: 'Source Sans 3', sans-serif;
    font-size: 13px;
    color: var(--text);
    line-height: 16.5px;
  }
  .contacts li { display: flex; align-items: center; gap: 5px; }
  .contacts svg { width: 11px; height: 11px; fill: var(--teal); flex: none; }
  .address {
    position: absolute; left: 240px; top: 184px;
    font-family: 'Source Sans 3', sans-serif;
    font-size: 13px;
    line-height: 16px;
    color: var(--text);
    font-style: normal;
  }

  /* back */
  .back__pattern {
    position: absolute; left: 0; top: 0;
    width: 100%; height: 250px;
    background: linear-gradient(to bottom, var(--card-pattern) 0%, var(--card-pattern) 70%, var(--card) 100%);
  }
  .back__brand {
    position: absolute; left: 330px; top: 125px;
    font-family: 'Quicksand', sans-serif;
    font-weight: 700;
    font-size: 17px;
    color: var(--teal);
  }
  .back__web {
    position: absolute; left: 0; right: 0; top: 224px;
    text-align: center;
    font-family: 'Montserrat', sans-serif;
    font-size: 14px;
    color: var(--text);
  }
  .back__web .accent { color: var(--teal); }
</style>
</head>
<body>
<main class="stage">
  <section class="card card--front" aria-label="Business card front">
    <div class="brand">
      <span class="brand__dot"></span>
      <p class="brand__name">Delmer's<br>Pressure Washing Services</p>
    </div>
    <span class="divider"></span>
    <div class="person">
      <p class="person__name">Delmer <span class="surname">Ortega</span></p>
      <p class="person__role">Managing Director</p>
    </div>
    <ul class="contacts">
      <li><svg viewBox="0 0 12 12"><path d="M1 4c0-2 2-3 5-3s5 1 5 3l-2 1-1-1H4L3 5 1 4zm2 2h6l1 4H2l1-4zm3 1a1.2 1.2 0 1 0 0 2.4A1.2 1.2 0 0 0 6 7z"/></svg>559-555 0142</li>
      <li><svg viewBox="0 0 12 12"><path d="M0 2h12v8H0z"/><path d="M1 3l5 4 5-4" fill="none" stroke="var(--card)" stroke-width="1"/></svg>info@delmerswash.com</li>
      <li><svg viewBox="0 0 12 12"><circle cx="6" cy="6" r="5.5"/><path d="M3 4c1-1 2 0 2 1s-1 1 0 2 1 2 0 3M8 2c-1 1 0 2 1 2s1 1 1 2" fill="none" stroke="var(--card)" stroke-width="1"/></svg>www.delmerswash.com</li>
    </ul>
    <address class="address">Suite 4, 218 Orchard Lane,<br>Fresno, California 93721.</address>
  </section>

  <section class="card card--back" aria-label="Business card back">
    <div class="back__pattern" role="img" aria-label="Faint repeating brand mark pattern"></div>
    <p class="back__brand">Delmer's</p>
    <p class="back__web">www.<span class="accent">delmerswash</span>.com</p>
  </section>
</main>
</body>
</html>
```